Presentation Folder Design for Photographer

Professional photographer requires a presentation folder for marketing.
I specialise in architecture, corporate & commercial photography. The folder will be used to promote my architectural photography services to real estate, accomodation & architect clients.

I'm looking for a modern clean design that complements my logo with complimentary text & colours. I want to use some images in the design, probably a mix of images not just architectural. I need a print ready design in PDF as well as a PSD file that I can possibly edit / update images later on.

The folder will be a double sided design with no need for pockets included in the design. Overall dimensions are 430mm ( folded down the centre ) x 315mm with a 5mm trim & bleed.

The layout would be as follows :

Front cover - Logo + maybe some images or some other design work.

Inside front cover - Some text about my services.

ARCHITECTURE
Commercial Residential Real Estate Drone Floorpans Accommodation

CORPORATE
Studio Headshots Environmental Portraits Staff Photography

COMMERCIAL
Product Advertising Fashion Event Stock

Inside back cover - no text as a seperate price list will sit here.

Outside back cover - I was thinking of having a collage of images worked into
the design but open to the designers input as well.
I also have another logo with phone number & web address
I would like on the back cover - Will be included in the files
provided.

I have a black background & white background version of my logo I will include both for the design work. I'm trying to get away from an all black design so if using the black logo I don't want a completely black page design, just becomes to heavy.

I'm redoing my website soon so please base the folder design around my logo text & colours not my current website as it's very outdated.

Logo brand guide is as follows

Main Font Font: Reislust
Main Font Color: #fff
Slogan Font Font: Ubuntu Bold
Monogram Font Font: Venti Medium
Container Color: #fff

Please respect the copyright on the images provided and delete all content once the design has been completed.
Thanks.

Need extra days to review

```html
<!DOCTYPE html>
<html lang="en">
<head>
<meta charset="utf-8">
<title>Frame and Field – Presentation Folder</title>
<link href="https://fonts.googleapis.com/css2?family=Josefin+Sans:wght@300;400&family=Ubuntu:wght@400;500;700&display=swap" rel="stylesheet">
<style>
  :root {
    --backdrop: #e6e7e9;
    --ink: #161616;
    --paper: #ffffff;
    --gold: #c9a55a;
    --gold-line: #b8954c;
    --white: #ffffff;
  }
  * { margin: 0; padding: 0; box-sizing: border-box; }
  html, body { width: 850px; height: 1200px; overflow: hidden; background: var(--backdrop); }
  .canvas { position: relative; width: 850px; height: 1200px; }

  .spread { position: absolute; box-shadow: 0 3px 8px rgba(0,0,0,.25); }
  .spread--outside { left: 69px; top: 54px; width: 707px; height: 519px; }
  .spread--inside { left: 66px; top: 622px; width: 712px; height: 518px; }

  .page { position: absolute; top: 0; height: 100%; overflow: hidden; }
  .page--back { left: 0; width: 353px; background: var(--ink); }
  .page--front { left: 353px; width: 354px; background: var(--paper); }
  .page--inside-left { left: 0; width: 355px; background: var(--ink); }
  .page--inside-right { left: 355px; width: 357px; background: linear-gradient(90deg, #fff 75%, #ececec); }

  .photo { position: absolute; }
  .collage .photo { width: 117px; height: 118px; }

  .focus-frame {
    position: absolute; left: 73px; top: 82px; width: 204px; height: 204px;
    border: 2px solid rgba(255,255,255,.85);
  }
  .focus-frame__veil { position: absolute; left: 45px; top: 36px; width: 115px; height: 117px; background: rgba(60,60,60,.4); }

  .gold-rule { position: absolute; left: 0; width: 100%; height: 3px;
    background: linear-gradient(90deg, var(--gold-line), #e6cf8f, var(--gold-line)); }

  .brand-name {
    font-family: "Josefin Sans", sans-serif; font-weight: 300;
    letter-spacing: .14em; white-space: nowrap;
  }
  .back-name { position: absolute; left: 0; width: 100%; text-align: center; top: 430px; font-size: 21px; color: var(--white); }
  .back-contact {
    position: absolute; left: 0; width: 100%; text-align: center; top: 457px;
    font-family: "Ubuntu", sans-serif; font-weight: 700; font-size: 6.5px;
    letter-spacing: .28em; color: var(--gold); white-space: nowrap;
  }
  .back-contact span + span { margin-left: 10px; }

  .lockup { position: absolute; display: flex; align-items: center; gap: 8px; }
  .lockup__mark { border: 1.5px solid var(--gold); flex: none; }
  .lockup--front { left: 99px; top: 418px; }
  .lockup--front .lockup__mark { width: 36px; height: 36px; }
  .lockup--front .brand-name { font-size: 10px; color: var(--ink); }
  .lockup--inside { left: 88px; top: 220px; gap: 10px; }
  .lockup--inside .lockup__mark { width: 40px; height: 40px; }
  .lockup--inside .brand-name { font-size: 11.5px; color: var(--white); }

  .web {
    position: absolute; font-family: "Ubuntu", sans-serif; font-weight: 700;
    font-size: 8.5px; letter-spacing: .32em; white-space: nowrap;
  }
  .web--front { left: 0; width: 100%; text-align: center; top: 483px; color: var(--ink); }
  .web--inside { left: 24px; top: 483px; color: var(--white); }

  .services { position: absolute; left: 24px; top: 318px; list-style: none; }
  .service { margin-bottom: 19px; }
  .service__title { font-family: "Ubuntu", sans-serif; font-weight: 400; font-size: 12px; color: var(--gold); letter-spacing: .02em; line-height: 14px; }
  .service__items { font-family: "Ubuntu", sans-serif; font-size: 8.6px; color: var(--white); line-height: 12px; }
</style>
</head>
<body>
<div class="canvas">

  <section class="spread spread--outside">
    <div class="page page--back">
      <div class="collage">
        <div class="photo" style="left:0;top:0;background:linear-gradient(180deg,#d8d2c6 60%,#8a8e94)" role="img" aria-label="Bright bedroom with wall map and curtains"></div>
        <div class="photo" style="left:118px;top:0;background:linear-gradient(180deg,#6e7a3c 55%,#d9d6dc)" role="img" aria-label="Fashion portrait in a garden with wisteria"></div>
        <div class="photo" style="left:236px;top:0;background:linear-gradient(180deg,#c9b9a2 50%,#e8e4df)" role="img" aria-label="Hotel bedroom with white bedding"></div>
        <div class="photo" style="left:0;top:120px;background:linear-gradient(180deg,#e4e2dc 45%,#3a3532)" role="img" aria-label="Kitchen with yellow bar stools"></div>
        <div class="photo" style="left:118px;top:120px;background:#d6d2d2" role="img" aria-label="Fashion portrait in pink"></div>
        <div class="photo" style="left:236px;top:120px;background:linear-gradient(180deg,#e0ddd6 55%,#4b4641)" role="img" aria-label="Kitchen with timber stools"></div>
        <div class="photo" style="left:0;top:240px;background:linear-gradient(180deg,#2f4d8a 45%,#4b5436)" role="img" aria-label="Heritage homestead at dusk"></div>
        <div class="photo" style="left:118px;top:240px;background:linear-gradient(180deg,#2a2a2a 45%,#b3242a 70%,#3a3a3a)" role="img" aria-label="Corporate portrait beside a red sports car"></div>
        <div class="photo" style="left:236px;top:240px;background:linear-gradient(180deg,#6d93c6 35%,#dfe2e6 70%,#5a5a5a)" role="img" aria-label="Modern building facade against blue sky"></div>
      </div>
      <div class="focus-frame"><div class="focus-frame__veil"></div></div>
      <div class="gold-rule" style="top:362px"></div>
      <h2 class="brand-name back-name">FRAME AND FIELD</h2>
      <p class="back-contact"><span>Ph 0400 123 456</span><span>www.frameandfield.com.au</span></p>
    </div>

    <div class="page page--front">
      <div class="photo" style="left:0;top:0;width:354px;height:362px;background:linear-gradient(180deg,#7a96c4 0%,#b9b2aa 22%,#4b4d50 30%,#4b4d50 52%,#9c4a2c 60%,#8a4428 75%,#5c6a2e 82%)" role="img" aria-label="Modern timber house with deck at twilight"></div>
      <div class="gold-rule" style="top:362px"></div>
      <div class="lockup lockup--front">
        <span class="lockup__mark"></span>
        <span class="brand-name">FRAME AND FIELD</span>
      </div>
      <p class="web web--front">www.frameandfield.com.au</p>
    </div>
  </section>

  <section class="spread spread--inside">
    <div class="page page--inside-left">
      <div class="photo" style="left:3px;top:50px;width:117px;height:120px;background:linear-gradient(180deg,#cdbf9f 35%,#eeede9 40%,#6a5c4c)" role="img" aria-label="White kitchen island with artwork"></div>
      <div class="photo" style="left:121px;top:50px;width:117px;height:120px;background:radial-gradient(ellipse 40% 45% at 50% 45%,#cfd0d2 60%,#1a1a1a 62%)" role="img" aria-label="Product shot of a wristwatch"></div>
      <div class="photo" style="left:240px;top:50px;width:106px;height:120px;background:linear-gradient(180deg,#3a3a3a 40%,#f0f0f0 42%,#f0f0f0 75%,#555)" role="img" aria-label="Modern bathroom vanity"></div>

      <div class="lockup lockup--inside">
        <span class="lockup__mark"></span>
        <span class="brand-name">FRAME AND FIELD</span>
      </div>

      <ul class="services">
        <li class="service">
          <h3 class="service__title">ARCHITECTURE</h3>
          <p class="service__items">Commercial Residential Real Estate Drone Floorpans Accommodation</p>
        </li>
        <li class="service">
          <h3 class="service__title">CORPORATE</h3>
          <p class="service__items">Studio Headshots Environmental Portraits Staff Photography</p>
        </li>
        <li class="service">
          <h3 class="service__title">COMMERCIAL</h3>
          <p class="service__items">Product Advertising Fashion Event Stock</p>
        </li>
      </ul>

      <p class="web web--inside">www.frameandfield.com.au</p>
    </div>
    <div class="page page--inside-right"></div>
  </section>

</div>
</body>
</html>
```